Website design for an events management company

What we need is the design of a website to be used by an events management company, the company is called "Vanto Events Management" and the website is expected to contain the following sections:
1) Homepage
2) Who are we?
3) Mission / Vision / Core values
4) Why to choose Vanto?
5) Past experience
6) Duties or provided services (Scientific Program Duties, Accreditation, Fund Raising, Accommodations, Social Activities, Transportation, Marketing of the Event, Publications and printed materials, Secretarial Work and Media Coverage)
7) References
8) Contact Us page (will probably contain a contact us form plus email, address and a google map)

Attached for your reference the company's logo

Expected that the winner should deliver the designs of at least two pages (the homepage plus an inner page) plus of course all the used graphics, images ... etc.

Thanks

Target Market(s)

The design need to target scientific events and not public events, for example the company doesn't organize music concerts ... etc., it organizes only scientific events so please target business users (i.e. doctors, engineers, scientisits ... etc) while making the designs, including the correct colors, images and icons

Industry/Entity Type

It Company

Number of Pages Required

2 page

Requirements
Must have
• One homepage
• One inner page
• All the used graphics and images
Nice to have
• More than two pages

```html
<!DOCTYPE html>
<html lang="en">
<head>
<meta charset="utf-8">
<title>Vanto Events Management</title>
<link rel="stylesheet" href="https://fonts.googleapis.com/css2?family=Ubuntu:wght@400;500&family=Open+Sans:wght@400;600&display=swap">
<style>
:root{
  --orange:#f39a1e;
  --blue:#2f93c6;
  --blue-dark:#1b5e8a;
  --nav-top:#4db3de;
  --nav-bottom:#2a8fc0;
  --nav-active:#1d1d1d;
  --purple:#7b1f7a;
  --ink:#333;
  --muted:#555;
  --soft:#f6f6f6;
  --line:#e4e4e4;
  --footer:#0b3c61;
  --footer-base:#0a2236;
  --red:#e8303a;
}
*{box-sizing:border-box;margin:0;padding:0}
html,body{width:1200px;height:2525px;overflow:hidden}
body{font-family:"Open Sans",Arial,sans-serif;color:var(--ink);background:#fff;font-size:12px}
.wrap{width:1002px;margin:0 auto;position:relative}

/* header */
.topbar{height:116px}
.topbar .wrap{height:116px}
.contact-mini{position:absolute;left:0;top:34px}
.contact-mini .phone{color:var(--orange);font-size:18px;font-weight:600;display:flex;align-items:center;gap:12px}
.contact-mini .mail{font-size:14px;color:#444;margin:6px 0 0 32px}
.brand{position:absolute;left:50%;top:26px;transform:translateX(-50%);text-align:center}
.brand .name{font-family:"Ubuntu",sans-serif;font-size:40px;font-weight:500;color:#555;display:flex;align-items:center;gap:8px;line-height:1}
.brand .name i{display:block;width:22px;height:22px;border-radius:50%;background:var(--purple)}
.brand .tag{font-size:11px;color:#666;margin-top:6px;white-space:nowrap}
.actions{position:absolute;right:2px;top:44px;display:flex;gap:10px}
.btn{height:33px;display:flex;align-items:center;justify-content:center;color:#fff;font-size:13px;border-radius:2px}
.btn-register{width:88px;background:var(--purple)}
.btn-login{width:69px;background:var(--blue)}
.btn-search{width:37px;border:1px solid #ddd;background:#fff}

.nav{height:67px;background:linear-gradient(var(--nav-top),var(--nav-bottom))}
.nav ul{list-style:none;display:flex;height:67px}
.nav li{color:#fff;font-family:"Ubuntu",sans-serif;font-size:13px;font-weight:400;padding:0 16px;display:flex;align-items:center;text-transform:uppercase;white-space:nowrap}
.nav li.active{background:var(--nav-active);padding:0 20px}

/* hero */
.hero{height:596px;position:relative;background:linear-gradient(110deg,#a9c4b9 0%,#d7dcd8 35%,#8fb3c8 60%,#4f6f8d 100%)}
.hero-caption{position:absolute;left:88px;top:214px;width:382px;height:222px;background:rgba(40,40,40,.62);padding:22px 30px 0 36px;color:#fff;overflow:hidden}
.hero-caption h1{font-family:"Ubuntu",sans-serif;font-weight:500;font-size:44px;line-height:1;white-space:nowrap}
.hero-caption h2{font-family:"Ubuntu",sans-serif;font-weight:400;font-size:28px;line-height:1;margin:10px 0 14px;white-space:nowrap}
.hero-caption p{font-size:12px;line-height:21px}
.hero-arrow{position:absolute;top:478px;width:32px;height:32px;border-radius:50%;background:rgba(60,60,60,.7);display:flex;align-items:center;justify-content:center}
.hero-arrow.prev{left:38px}.hero-arrow.next{right:14px}

/* welcome */
.welcome{height:209px;background:var(--soft);border-bottom:1px solid var(--line);text-align:center;padding-top:42px}
.section-title{font-family:"Ubuntu",sans-serif;font-weight:400;font-size:30px;color:#333}
.section-title span{color:var(--blue)}
.welcome p{width:910px;margin:20px auto 0;font-size:11.5px;line-height:22px;color:var(--muted)}

/* features */
.features{height:362px;border-bottom:1px solid var(--line)}
.features .wrap{display:grid;grid-template-columns:repeat(4,200px);column-gap:64px;padding:52px 0 0 3px}
.feature{width:200px;text-align:center}
.feature-icon{width:122px;height:122px;margin:0 auto;border-radius:50%;border:9px solid #efefef;background:#fff;display:flex;align-items:center;justify-content:center;position:relative}
.feature-icon::after{content:"";position:absolute;bottom:-30px;left:-10px;width:142px;height:12px;border-radius:50%;background:radial-gradient(rgba(0,0,0,.12),transparent 70%)}
.feature h3{font-family:"Ubuntu",sans-serif;font-weight:400;font-size:17px;margin-top:44px;color:#333}
.feature p{font-size:11px;line-height:20px;color:var(--muted);margin-top:10px}

/* about */
.about{height:409px;background:var(--soft);border-bottom:1px solid var(--line)}
.about .wrap{display:flex;gap:35px;padding-top:69px}
.video-frame{width:394px;height:286px;background:#fff;border:1px solid #ddd;padding:10px;flex:none}
.video-frame .shot{width:100%;height:100%;background:linear-gradient(120deg,#dfe6ea,#b8c7d2 55%,#8c9fb0);display:flex;align-items:center;justify-content:center}
.play{width:40px;height:28px;background:#fff;border-radius:6px;display:flex;align-items:center;justify-content:center}
.about-text{flex:1}
.about-text h2{font-family:"Ubuntu",sans-serif;font-weight:400;font-size:22px;margin:-2px 0 10px}
.about-text h2 span{color:var(--blue)}
.about-text p{font-size:10.8px;line-height:18px;color:var(--muted);text-align:justify;margin-bottom:17px}
.btn-more{width:132px;height:38px;background:var(--blue-dark);color:#fff;font-size:13px;display:flex;align-items:center;justify-content:center;gap:8px;border-radius:2px;margin-top:6px}

/* events */
.events{height:458px;text-align:center;padding-top:36px}
.events .section-title{font-size:26px;text-transform:uppercase}
.cards{display:flex;gap:10px;margin-top:30px;text-align:left}
.card{width:243px;height:315px;background:#fff;box-shadow:0 1px 4px rgba(0,0,0,.18)}
.card .thumb{height:178px}
.card h4{font-weight:400;font-size:16px;color:#333;margin:15px 15px 6px}
.card p{font-size:11.5px;line-height:20px;color:var(--muted);margin:0 15px}
.card .meta{margin-top:14px;border-top:1px solid #eee;height:42px;padding:0 15px;display:flex;align-items:center;justify-content:space-between;color:var(--blue-dark);font-size:12px}
.t1{background:linear-gradient(135deg,#c9d6e2,#6f8aa6)}
.t2{background:linear-gradient(135deg,#e6e9ec,#8d99a8)}
.t3{background:linear-gradient(135deg,#d8dde2,#7b8796)}
.t4{background:linear-gradient(180deg,#c8cfd6,#8a8f96 70%,#b9a487)}

/* footer */
.footer{height:229px;background:var(--footer);color:#fff}
.footer .wrap{display:flex;padding-top:38px}
.footer h5{font-family:"Ubuntu",sans-serif;font-weight:400;font-size:15px;text-transform:uppercase;margin-bottom:14px}
.col-ref{width:273px}.col-ref h5{font-size:20px;margin-top:-4px;margin-bottom:12px}
.col-ref p{width:215px}
.col-news{width:310px}
.col-news p{width:230px}
.col-info{width:173px}
.col-contact{flex:1}
.footer p{font-size:11.5px;line-height:19px}
.social{display:flex;gap:6px;margin-top:16px}
.social i{width:18px;height:18px;background:#fff;border-radius:3px;display:block}
.subscribe{display:flex;margin-top:16px}
.subscribe .field{width:160px;height:40px;background:#fff;color:#333;font-size:11.5px;display:flex;align-items:center;padding-left:14px}
.subscribe .go{width:81px;height:40px;background:var(--red);font-size:11px;display:flex;align-items:center;justify-content:center}
.col-info ul{list-style:none}
.col-info li{font-size:12px;line-height:24px}
.col-contact .addr{font-size:12.5px;line-height:22px}
.col-contact .row{display:flex;align-items:center;gap:16px;font-size:13px;margin-top:10px}
.copyright{height:79px;background:var(--footer-base);color:#fff;font-size:12px;display:flex;align-items:center;justify-content:center}
</style>
</head>
<body>

<header class="topbar">
  <div class="wrap">
    <div class="contact-mini">
      <div class="phone">
        <svg width="20" height="20" viewBox="0 0 24 24"><path d="M6.6 10.8a15 15 0 0 0 6.6 6.6l2.2-2.2c.3-.3.7-.4 1-.2 1.1.4 2.3.6 3.6.6.6 0 1 .4 1 1V20c0 .6-.4 1-1 1A17 17 0 0 1 3 4c0-.6.4-1 1-1h3.5c.6 0 1 .4 1 1 0 1.3.2 2.5.6 3.6.1.3 0 .7-.2 1z" fill="#f39a1e"/></svg>
        Ph: (09) 5120 7742
      </div>
      <div class="mail">info@vantoevents.com</div>
    </div>
    <div class="brand">
      <div class="name"><i></i>Vanto</div>
      <div class="tag">Vanto Events Management</div>
    </div>
    <div class="actions">
      <div class="btn btn-register">REGISTER</div>
      <div class="btn btn-login">LOGIN</div>
      <div class="btn btn-search"><svg width="12" height="12" viewBox="0 0 12 12"><circle cx="5" cy="5" r="3.5" fill="none" stroke="#666" stroke-width="1.5"/><path d="M7.5 7.5l3 3" stroke="#666" stroke-width="1.5"/></svg></div>
    </div>
  </div>
</header>

<nav class="nav">
  <div class="wrap">
    <ul>
      <li class="active">Home</li><li>Who are we</li><li>Mission</li><li>Vision</li><li>Why to choose Vanto?</li><li>Past experience</li><li>Services</li><li>References</li><li>Contact us</li>
    </ul>
  </div>
</nav>

<section class="hero" role="img" aria-label="Photo of a team of three colleagues working together at a laptop in a bright office">
  <div class="hero-caption">
    <h1>VANTO EVENT</h1>
    <h2>MANAGEMENT</h2>
    <p>Lorem ipsum dolor sit amet, consectetur adipiscing elit, sed do eiusmod tempor incididunt ut labore Lorem ipsum dolor sit amet, consectetur adipiscing elit, sed do eiusmod</p>
  </div>
  <div class="hero-arrow prev"><svg width="10" height="12" viewBox="0 0 10 12"><path d="M7 1L2 6l5 5" stroke="#fff" stroke-width="2" fill="none"/></svg></div>
  <div class="hero-arrow next"><svg width="10" height="12" viewBox="0 0 10 12"><path d="M3 1l5 5-5 5" stroke="#fff" stroke-width="2" fill="none"/></svg></div>
</section>

<section class="welcome">
  <h2 class="section-title">Welcome To <span>Vanto Event management</span></h2>
  <p>Lorem ipsum dolor sit amet, consectetur adipiscing elit, sed do eiusmod tempor incididunt ut labore et dolore magna aliqua. Ut enim ad minim veniam, quis nostrud exercitation ullamco laboris nisi ut aliquip ex ea commodo consequat. Duis aute irure dolor in reprehenderit in voluptate velit esse cillum dolore eu fugiat nulla pariatur. Excepteur sint occaecat cupidatat non proident, sunt in culpa qui officia deserunt mollit anim id est laborum</p>
</section>

<section class="features">
  <div class="wrap">
    <div class="feature">
      <div class="feature-icon"><svg width="40" height="36" viewBox="0 0 40 36" fill="#3a8fc6"><circle cx="20" cy="9" r="6"/><circle cx="8" cy="12" r="4.5"/><circle cx="32" cy="12" r="4.5"/><path d="M10 34v-8a10 10 0 0 1 20 0v8z"/><path d="M0 32v-6a8 8 0 0 1 11-7 13 13 0 0 0-3 8v5zM40 32v-6a8 8 0 0 0-11-7 13 13 0 0 1 3 8v5z"/></svg></div>
      <h3>WHO ARE WE</h3>
      <p>Lorem ipsum dolor sit amet, conse adipisic ing elit, sed do eiusmod tempor incididunt ut labore et dolore</p>
    </div>
    <div class="feature">
      <div class="feature-icon"><svg width="30" height="40" viewBox="0 0 30 40"><path d="M15 3a11 11 0 0 0-6 20v5h12v-5a11 11 0 0 0-6-20z" fill="none" stroke="#e2312f" stroke-width="3"/><rect x="9" y="31" width="12" height="3" fill="#e2312f"/><rect x="11" y="36" width="8" height="3" fill="#e2312f"/></svg></div>
      <h3>MISSION</h3>
      <p>Lorem ipsum dolor sit amet, conse adipisic ing elit, sed do eiusmod tempor incididunt ut labore et dolore</p>
    </div>
    <div class="feature">
      <div class="feature-icon"><svg width="40" height="36" viewBox="0 0 40 36" fill="#f39a1e"><path d="M4 12h9a5 5 0 1 1 8 0h9v9a5 5 0 1 0 0 8v5H4v-9a5 5 0 1 0 0-8z"/></svg></div>
      <h3>VISION</h3>
      <p>Lorem ipsum dolor sit amet, conse adipisic ing elit, sed do eiusmod tempor incididunt ut labore et dolore</p>
    </div>
    <div class="feature">
      <div class="feature-icon"><svg width="40" height="40" viewBox="0 0 40 40" fill="#6d2c8f"><path d="M18 6A16 16 0 1 0 34 22H18z"/><path d="M22 2v16h16A16 16 0 0 0 22 2z"/></svg></div>
      <h3>SERVICES</h3>
      <p>Lorem ipsum dolor sit amet, conse adipisic ing elit, sed do eiusmod tempor incididunt ut labore et dolore</p>
    </div>
  </div>
</section>

<section class="about">
  <div class="wrap">
    <div class="video-frame">
      <div class="shot" role="img" aria-label="Video still of a presenter pointing at a chart in front of colleagues">
        <div class="play"><svg width="12" height="14" viewBox="0 0 12 14"><path d="M1 1l10 6-10 6z" fill="#333"/></svg></div>
      </div>
    </div>
    <div class="about-text">
      <h2>Event <span>Management</span></h2>
      <p>Lorem ipsum dolor sit amet, consectetur adipiscing elit, sed do eiusmod tempor incididunt ut labore et dolore magna aliqua. Ut enim ad minim veniam, quis nostrud exercitation ullamco laboris nisi ut aliquip ex ea commodo consequat. Duis aute irure dolor in reprehenderit in voluptate velit esse cillum dolore .</p>
      <p>Lorem ipsum dolor sit amet, consectetur adipiscing elit, sed do eiusmod tempor incididunt ut labore et dolore magna aliqua. Ut enim ad minim veniam, quis nostrud exercitation ullamco laboris nisi ut aliquip ex ea commodo consequat. Duis aute irure dolor in reprehenderit in voluptate velit esse cillum dolore .</p>
      <p>Tempor incididunt ut labore et dolore magna aliqua. Ut en im ad minim veniam, quis nostrud exercitation ullamco laboris nisi ut aliquip ex ea commodo consequat. Duis aute irure dolor in reprehenderit in voluptate</p>
      <div class="btn-more">MORE INFO <svg width="13" height="13" viewBox="0 0 14 14"><circle cx="7" cy="7" r="7" fill="#fff"/><path d="M6 4l3 3-3 3" stroke="#1b5e8a" stroke-width="1.8" fill="none"/></svg></div>
    </div>
  </div>
</section>

<section class="events">
  <div class="wrap">
    <h2 class="section-title">RECENT <span>EVENT</span></h2>
    <div class="cards">
      <article class="card"><div class="thumb t1" role="img" aria-label="Photo of hands using a tablet over printed charts"></div><h4>Sed docendi copiosae</h4><p>Lorem ipsum dolor sit amet, consectur scing elit, sed do eiusmod tempor</p><div class="meta">July 25, 2015<svg width="8" height="8" viewBox="0 0 8 8"><path d="M1 1l6 6M7 3v4H3" stroke="#aaa" fill="none"/></svg></div></article>
      <article class="card"><div class="thumb t2" role="img" aria-label="Photo of a businessman in a suit in an office"></div><h4>Sed docendi copiosae</h4><p>Lorem ipsum dolor sit amet, consectur scing elit, sed do eiusmod tempor</p><div class="meta">July 25, 2015<svg width="8" height="8" viewBox="0 0 8 8"><path d="M1 1l6 6M7 3v4H3" stroke="#aaa" fill="none"/></svg></div></article>
      <article class="card"><div class="thumb t3" role="img" aria-label="Photo of colleagues in a meeting with a laptop"></div><h4>Sed docendi copiosae</h4><p>Lorem ipsum dolor sit amet, consectur scing elit, sed do eiusmod tempor</p><div class="meta">July 25, 2015<svg width="8" height="8" viewBox="0 0 8 8"><path d="M1 1l6 6M7 3v4H3" stroke="#aaa" fill="none"/></svg></div></article>
      <article class="card"><div class="thumb t4" role="img" aria-label="Photo of a businesswoman with a telescope on a rooftop above a city"></div><h4>Sed docendi copiosae</h4><p>Lorem ipsum dolor sit amet, consectur scing elit, sed do eiusmod tempor</p><div class="meta">July 25, 2015<svg width="8" height="8" viewBox="0 0 8 8"><path d="M1 1l6 6M7 3v4H3" stroke="#aaa" fill="none"/></svg></div></article>
    </div>
  </div>
</section>

<footer class="footer">
  <div class="wrap">
    <div class="col-ref">
      <h5>References</h5>
      <p>Lorem ipsum dolor sit amet, consectetur adipiscing elit, sed do eiusmod tempor incididunt ut labore et dolore magna aliqua. Ut enim ad minim veniam, quis nostrud</p>
      <div class="social"><i></i><i></i><i></i></div>
    </div>
    <div class="col-news">
      <h5>Join our newsletter</h5>
      <p>Excepteur sint occaecat cupidatat non proident, sunt in culpa qui</p>
      <div class="subscribe"><div class="field">Enter Name</div><div class="go">SUBSCRIBE</div></div>
    </div>
    <div class="col-info">
      <h5>Information</h5>
      <ul><li>Home</li><li>Services</li><li>Inspiration</li><li>Availability</li><li>Contact</li></ul>
    </div>
    <div class="col-contact">
      <h5>Contact us</h5>
      <div class="addr">2184 Birchfield Road Kansas City,<br>MO 64118</div>
      <div class="row"><svg width="18" height="18" viewBox="0 0 24 24"><path d="M6.6 10.8a15 15 0 0 0 6.6 6.6l2.2-2.2c.3-.3.7-.4 1-.2 1.1.4 2.3.6 3.6.6.6 0 1 .4 1 1V20c0 .6-.4 1-1 1A17 17 0 0 1 3 4c0-.6.4-1 1-1h3.5c.6 0 1 .4 1 1 0 1.3.2 2.5.6 3.6.1.3 0 .7-.2 1z" fill="none" stroke="#fff" stroke-width="1.5"/></svg>+1 &nbsp;(913) 555-0148</div>
      <div class="row"><svg width="18" height="14" viewBox="0 0 18 14"><rect x="1" y="1" width="16" height="12" fill="none" stroke="#fff" stroke-width="1.3"/><path d="M1 1l8 7 8-7" fill="none" stroke="#fff" stroke-width="1.3"/></svg>info@vantoevents.com</div>
    </div>
  </div>
</footer>
<div class="copyright">© Copyright 2015, &nbsp;All Rights Reserved</div>

</body>
</html>
```